Site Update/Merger: TWR Dynamics

We want to take some content (not ALL the content, but only what is specified) from two or our sites and combine into one
The New Website is in Wordpress too.
The new site needs to be a nice merge between these sites:
◦ https://brontavo-works.example/
◦ https://taskmira-launch.example/
Theme/topic: this is an Engineering site
The blog must be included on the home page (maybe smaller), and also on the Systems Engineering page (maybe a little bigger, allow the user to browse through all blogs)
Instructions and visual aids:
Step 1: SEE BRIEFING IN THE PDF ATTACHED
Step 2: some pictures for your reference (referenced in the PDF)

```html
<!DOCTYPE html>
<html lang="en">
<head>
<meta charset="utf-8">
<title>Contact Us – TWR Dynamics</title>
<link href="https://fonts.googleapis.com/css2?family=IBM+Plex+Sans:wght@400;500;700&display=swap" rel="stylesheet">
<style>
  :root {
    --brand-blue: #3a3fa0;
    --ink: #111111;
    --navy: #0b1630;
    --footer-bg: #1c1b1d;
    --footer-text: #ffffff;
    --divider: #3a393c;
    --card-bg: rgba(246, 247, 249, 0.95);
  }
  * { margin: 0; padding: 0; box-sizing: border-box; }
  html, body { width: 1200px; height: 706px; overflow: hidden; }
  body {
    position: relative;
    font-family: "IBM Plex Sans", Arial, sans-serif;
    color: var(--ink);
    background: #fff;
  }
  a { color: inherit; text-decoration: none; }

  .site-header { position: absolute; left: 0; top: 0; width: 1200px; height: 86px; background: #fff; }
  .brand {
    position: absolute; left: 133px; top: 26px;
    font-size: 26px; font-weight: 700; color: var(--brand-blue); letter-spacing: -0.3px;
  }
  .main-nav { position: absolute; top: 32px; left: 0; width: 1200px; }
  .main-nav a {
    position: absolute; font-size: 14.5px; font-weight: 500; text-transform: uppercase; line-height: 18px;
  }
  .main-nav .nav-home { left: 786px; }
  .main-nav .nav-services { left: 874px; }
  .main-nav .nav-contact { left: 982px; }
  .main-nav .nav-contact::after {
    content: ""; position: absolute; left: 2px; right: 0; top: 22px; height: 2px; background: var(--ink);
  }

  .hero {
    position: absolute; left: 0; top: 86px; width: 1200px; height: 421px;
    background:
      radial-gradient(ellipse at 50% 80%, #2e5f9a 0%, transparent 55%),
      linear-gradient(135deg, #0d2346 0%, #1d4a80 40%, #15365f 65%, #0a1c38 100%);
  }
  .contact-card {
    position: absolute; left: 295px; top: 84px; width: 632px; height: 272px;
    background: var(--card-bg); text-align: center;
  }
  .contact-card .icon-badge {
    position: absolute; left: 288px; top: 52px; width: 56px; height: 56px;
    border-radius: 50%; background: var(--navy);
  }
  .contact-card .icon-badge svg { position: absolute; left: 16px; top: 18px; }
  .contact-card .card-text {
    position: absolute; left: 0; top: 132px; width: 632px;
    font-size: 25.5px; line-height: 38px; font-weight: 400;
  }

  .site-footer {
    position: absolute; left: 0; top: 507px; width: 1200px; height: 199px;
    background: var(--footer-bg); color: var(--footer-text);
  }
  .footer-brand { position: absolute; left: 133px; top: 46px; font-size: 24px; font-weight: 700; }
  .footer-nav a {
    position: absolute; left: 307px; font-size: 11.5px; text-transform: uppercase; line-height: 14px;
  }
  .footer-nav .f-home { top: 39px; }
  .footer-nav .f-services { top: 64px; }
  .footer-nav .f-contact { top: 89px; }
  .footer-contact p { position: absolute; left: 845px; font-size: 12.8px; line-height: 16px; white-space: nowrap; }
  .footer-contact svg { position: absolute; left: -18px; top: 4px; }
  .footer-contact .f-location { top: 47px; }
  .footer-contact .f-email { top: 79px; }
  .footer-divider { position: absolute; left: 137px; top: 134px; width: 933px; height: 1px; background: var(--divider); }
  .copyright { position: absolute; left: 0; top: 161px; width: 1200px; text-align: center; font-size: 10px; }
</style>
</head>
<body>
  <header class="site-header">
    <a class="brand" href="#">TWR Dynamics</a>
    <nav class="main-nav">
      <a class="nav-home" href="#">Home</a>
      <a class="nav-services" href="#">Services</a>
      <a class="nav-contact" href="#">Contact Us</a>
    </nav>
  </header>

  <section class="hero" role="img" aria-label="Close-up photograph of a blue circuit board with chips and traces">
    <div class="contact-card">
      <div class="icon-badge">
        <svg width="24" height="19" viewBox="0 0 24 19" aria-hidden="true">
          <path d="M0 2a2 2 0 0 1 2-2h20a2 2 0 0 1 2 2v1L12 10 0 3z" fill="#fff"/>
          <path d="M0 5.5l12 7 12-7V17a2 2 0 0 1-2 2H2a2 2 0 0 1-2-2z" fill="#fff"/>
        </svg>
      </div>
      <p class="card-text">Email to<br>info@taskmira-launch.example</p>
    </div>
  </section>

  <footer class="site-footer">
    <div class="footer-brand">TWR Dynamics</div>
    <nav class="footer-nav">
      <a class="f-home" href="#">Home</a>
      <a class="f-services" href="#">Services</a>
      <a class="f-contact" href="#">Contact Us</a>
    </nav>
    <div class="footer-contact">
      <p class="f-location">
        <svg width="7" height="10" viewBox="0 0 7 10" aria-hidden="true"><path d="M3.5 0A3.5 3.5 0 0 0 0 3.5C0 6 3.5 10 3.5 10S7 6 7 3.5A3.5 3.5 0 0 0 3.5 0zm0 5A1.5 1.5 0 1 1 3.5 2a1.5 1.5 0 0 1 0 3z" fill="#fff"/></svg>
        North America Location: Harlow Bay, NC
      </p>
      <p class="f-email">
        <svg width="9" height="7" viewBox="0 0 24 19" aria-hidden="true" style="top:6px"><path d="M0 2a2 2 0 0 1 2-2h20a2 2 0 0 1 2 2v1L12 10 0 3z" fill="#fff"/><path d="M0 5.5l12 7 12-7V17a2 2 0 0 1-2 2H2a2 2 0 0 1-2-2z" fill="#fff"/></svg>
        Email: info@taskmira-launch.example
      </p>
    </div>
    <div class="footer-divider"></div>
    <p class="copyright">Copyright © 2021 All Rights Reserved</p>
  </footer>
</body>
</html>
```